House-share and Room Rental Website (With Focus on the Bedroom Landing Page)

Looking for website design for our House-share (executive accommodation) and room rental business.

Our company name is: Lodvenra could also be written as LodVenra or lodvenra. Either is fine .. just looking for a nice clean catchy logo to go with the design.

EXAMPLES
These are examples of other websites in this field that are doing well. this is a kind of baseline.
https://kelbrin.com.au/
https://www.tuvaplex.com/
https://www.nestorvi.com/
https://www.quillsa.net/
https://www.pendlebarrow.com.au/

Our business model is to rent rooms to people looking for high-quality accommodation. We fill the gap between those looking to rent rooms and those with rooms to rent. However, our model is slightly different from those already on the market as we looking to fill a massive gap in the market delivering upmarket rooms for rent.(Executive Accommodation) also in the back end will be coupled with a self management process in the back end.

We offer executive style accommodation that stands out above the rest. With special extras like fire safety.. and management processes that create happier homes. We are looking for a web design package that can help us grow and scale our business. We need a design that is captivating

Our MAIN focus is having a room landing page that stands out from the rest... The core of our business will rely on the promotion of the rooms in a share house... so the whole design relies on the BEDROOM landing page to drive results.

Target Market(s)

We have 2 markets we are aiming at ... the first market is people offering rooms to rent who want the highest rental return. The second market is people looking to rent safe, high-quality rooms, in houses that are well managed and looked after.

Industry/Entity Type

Share Economy

Logo Text

LodVenra

Number of Pages Required

5+ page

Font styles to use
Sans Serif

Colors
3276b5

Requirements
Must have
• A messaging system whereby we can create direct communication between those offering rooms and those looking for rooms.
• A call to action that says " Schedule an Inspection"
• Landing page for promoting rooms
• A home page for showing stock.
• Profile page for those selling rooms
• Profile page for those looking for rooms.
• A scheduling calendar for booking inspections
Nice to have
• Pages where new residents can lock in a room.. pay bond and rents.. and sign contracts
• Notifications
• SMS capabilities in the backend.
Should not have
• No script or handwriting fonts.

```html
<!DOCTYPE html>
<html lang="en">
<head>
<meta charset="utf-8">
<title>LodVenra — Calloway Drive</title>
<link href="https://fonts.googleapis.com/css2?family=Lato:wght@300;400;700&display=swap" rel="stylesheet">
<style>
:root{
  --brand:#3276b5;
  --brand-soft:#4a86c5;
  --ink:#2b2b2b;
  --muted:#777;
  --line:#dcdcdc;
  --accent:#f7a80d;
  --page:#ffffff;
  --hero-a:#2f6d62;
  --hero-b:#e9e6e0;
  --band-a:#3a6ea3;
  --band-b:#254d7a;
}
*{box-sizing:border-box;margin:0;padding:0}
html,body{width:1200px;height:2913px;overflow:hidden;background:var(--page)}
body{font-family:'Lato',sans-serif;color:var(--ink);position:relative}
.abs{position:absolute}

.site-header{position:absolute;left:0;top:0;width:1200px;height:103px;background:#fff}
.brand-name{left:117px;top:32px;font-size:38px;font-weight:400;color:var(--brand);letter-spacing:1px}
.saved{left:852px;top:38px;width:34px;height:32px}
.account{left:916px;top:38px;display:flex;align-items:center;gap:14px;font-size:23px;color:#555}

.hero{left:0;top:103px;width:1200px;height:633px;background:linear-gradient(100deg,#f2f1ee 0%,#e6e3dd 30%,var(--hero-a) 45%,#3a7a6e 75%,#c9c6c0 100%)}
.gallery-tab{left:0;top:365px;width:87px;height:109px;background:rgba(255,255,255,.9);display:flex;align-items:center;justify-content:center;gap:14px}
.gallery-tab span{writing-mode:vertical-rl;font-size:14px;letter-spacing:1px;color:#333}

.room-card{left:654px;top:229px;width:428px;height:385px;background:#fff;padding:40px 42px 0 42px;box-shadow:0 2px 10px rgba(0,0,0,.08)}
.room-card h1{font-size:26px;font-weight:400;letter-spacing:1px;color:#333}
.room-card .fav{position:absolute;right:40px;top:42px}
.room-card p{margin-top:16px;font-size:14px;line-height:21px;color:#999;width:346px}
.facts{margin-top:20px;display:grid;grid-template-columns:170px 1fr;row-gap:26px;font-size:14px;font-weight:700;color:#333}
.facts div{display:flex;align-items:center;gap:14px}
.rent-btn{display:block;margin-top:30px;width:344px;height:46px;background:var(--accent);color:#fff;font-size:15px;font-weight:700;text-align:center;line-height:46px;letter-spacing:.5px}

.section-title{font-size:28px;font-weight:400;color:var(--brand);letter-spacing:.5px}
.details{left:117px;top:843px}
.details dl{margin-top:28px;display:grid;grid-template-columns:176px 1fr;row-gap:21px;font-size:17px}
.details dt{color:#888}
.details dd{color:#333;line-height:27px;margin-top:-5px}

.owner-card{left:777px;top:880px;width:268px;height:180px;border:1px solid var(--line)}
.avatar{left:851px;top:824px;width:120px;height:120px;border-radius:50%;border:5px solid #fff;box-shadow:0 0 0 1px var(--line);background:radial-gradient(circle at 50% 45%,#e8c9a8,#b9925e 70%,#8d6b46)}
.owner-name{left:777px;top:965px;width:268px;text-align:center;font-size:17px;color:#333}
.owner-role{left:777px;top:995px;width:268px;text-align:center;font-size:15px;color:#888}
.message-btn{left:835px;top:1033px;width:157px;height:45px;background:var(--brand-soft);color:#fff;font-size:17px;text-align:center;line-height:45px}
.share-title{left:777px;top:1143px;width:268px;text-align:center;font-size:16px;color:#333;letter-spacing:.5px}
.share{left:807px;top:1190px;display:flex;gap:32px}
.share span{width:48px;height:48px;border-radius:50%;background:var(--brand)}

.copy{width:570px;font-size:17px;line-height:27px;color:#333}
.copy p+p{margin-top:17px}
.features{display:flex;flex-direction:column;gap:26px;font-size:18px;color:#333}
.features .row{display:flex}
.features .item{display:flex;align-items:center;gap:18px}

.house{left:117px;top:1228px}
.owner{left:117px;top:2036px}
.prefs{left:117px;top:1758px}

.cta-band{left:0;top:2424px;width:1200px;height:404px;background:linear-gradient(100deg,#7ea0c6 0%,var(--band-a) 40%,var(--band-b) 100%)}
.cta-title{left:0;top:2515px;width:1200px;text-align:center;font-size:38px;line-height:54px;color:#fff;font-weight:400}
.cta-btn{left:416px;top:2659px;width:370px;height:60px;background:#fff;color:var(--brand);font-size:23px;text-align:center;line-height:60px}
.site-footer{left:0;top:2860px;width:1200px;text-align:center;font-size:14px;color:#777}
</style>
</head>
<body>
<svg width="0" height="0" style="position:absolute">
  <symbol id="tick" viewBox="0 0 32 32"><circle cx="16" cy="16" r="13" fill="none" stroke="#3276b5" stroke-width="2.4" stroke-dasharray="70 12" transform="rotate(-40 16 16)"/><path d="M9 16l5 5 11-12" fill="none" stroke="#3276b5" stroke-width="2.6" stroke-linecap="round" stroke-linejoin="round"/></symbol>
</svg>

<header class="site-header">
  <div class="abs brand-name">LodVenra</div>
  <svg class="abs saved" viewBox="0 0 34 32"><path d="M20 8l3 7 7 .6-5.4 4.7 1.7 7-6.3-3.9-6.3 3.9 1.7-7L10 15.6l7-.6z" fill="#555"/><circle cx="11" cy="9" r="8" fill="#f7a80d"/></svg>
  <div class="abs account"><svg width="24" height="26" viewBox="0 0 24 26"><circle cx="12" cy="7" r="6" fill="#666"/><path d="M0 26c0-8 5-12 12-12s12 4 12 12z" fill="#666"/></svg>My Account</div>
</header>

<section class="abs hero" role="img" aria-label="Photo of a bright bedroom with a made bed, ladder shelf and green feature wall"></section>
<div class="abs gallery-tab"><svg width="14" height="24" viewBox="0 0 14 24"><path d="M12 2L3 12l9 10" fill="none" stroke="#333" stroke-width="2.5"/></svg><span>IMAGES</span></div>

<article class="abs room-card">
  <h1>CALLOWAY DRIVE</h1>
  <svg class="fav" width="28" height="28" viewBox="0 0 28 28"><path d="M14 2l3.5 8 8.5.7-6.5 5.6 2 8.5L14 20.3 6.5 24.8l2-8.5L2 10.7l8.5-.7z" fill="none" stroke="#444" stroke-width="1.8"/></svg>
  <p>Lorem ipsum dolor sit amet, consectetur adipisci elit. Maecenas finibus diam:</p>
  <div class="facts">
    <div><svg width="36" height="22" viewBox="0 0 36 22"><rect x="1" y="2" width="34" height="17" fill="none" stroke="#3276b5" stroke-width="2.5"/><circle cx="18" cy="10.5" r="4.5" fill="#3276b5"/></svg>$200/WK</div>
    <div><svg width="28" height="28" viewBox="0 0 28 28"><rect x="2" y="5" width="24" height="21" fill="none" stroke="#3276b5" stroke-width="2.5"/><rect x="2" y="5" width="24" height="6" fill="#3276b5"/></svg>3 MONTHS MIN</div>
    <div><svg width="30" height="28" viewBox="0 0 30 28"><path d="M15 2L2 13h4v13h18V13h4z" fill="#3276b5"/></svg>SINGLE PERSON</div>
  </div>
  <a class="rent-btn">RENT THIS ROOM</a>
</article>

<section class="abs details">
  <h2 class="section-title">RENT DETAILS</h2>
  <dl>
    <dt>Room Size:</dt><dd>Single</dd>
    <dt>Rental Price:</dt><dd>190/pw rent + 40pw Consumables</dd>
    <dt>Date Available:</dt><dd>25 February 2019</dd>
    <dt>Min Time Stay:</dt><dd>3 Months</dd>
    <dt>Location:</dt><dd>Calloway Drive, BRENTMOOR HEIGHTS<br>Just 8 Min From the Airport and close to the city</dd>
  </dl>
</section>

<aside>
  <div class="abs owner-card"></div>
  <div class="abs avatar" role="img" aria-label="Portrait photo of the room owner"></div>
  <div class="abs owner-name">Marisa Feldholt</div>
  <div class="abs owner-role">Writer</div>
  <a class="abs message-btn">Message me</a>
  <div class="abs share-title">SHARE WITH FRIENDS</div>
  <div class="abs share"><span></span><span></span><span></span></div>
</aside>

<section class="abs house">
  <h2 class="section-title">ABOUT THE HOUSE</h2>
  <div class="copy" style="margin-top:30px">
    <p>Lorem ipsum dolor sit amet, consectetur adipiscing elit. Duis a sapien venenatis, accumsan orci nec,</p>
    <p>convallis tellus. Suspendisse sed rutrum libero. Mauris gravida posuere lacus, eu faucibus magna rhoncus ut. Pellentesque quis nisl dapibus, euismod diam vel, elementum justo. Nunc imperdiet lectus sed mauris condimentum aliquet.</p>
  </div>
  <div class="features" style="margin-top:28px">
    <div class="row"><div class="item" style="width:330px"><svg width="30" height="30"><use href="#tick"/></svg>Large Standing wardrobes</div><div class="item"><svg width="30" height="30"><use href="#tick"/></svg>Super fast internet</div></div>
    <div class="row"><div class="item" style="width:342px"><svg width="30" height="30"><use href="#tick"/></svg>42 inches TV + Castora</div><div class="item"><svg width="30" height="30"><use href="#tick"/></svg>Study/wrokstation</div></div>
    <div class="row"><div class="item" style="width:396px"><svg width="30" height="30"><use href="#tick"/></svg>Huge room with Queen sized bed</div><div class="item"><svg width="30" height="30"><use href="#tick"/></svg>New furniture</div></div>
  </div>
</section>

<section class="abs prefs">
  <h2 class="section-title">ROOM PREFERENCE</h2>
  <div class="features" style="margin-top:42px">
    <div class="row"><div class="item" style="width:282px"><svg width="30" height="30"><use href="#tick"/></svg>Non Smoking House</div><div class="item"><svg width="30" height="30"><use href="#tick"/></svg>Male &amp; Female</div></div>
    <div class="row"><div class="item"><svg width="30" height="30"><use href="#tick"/></svg>All ages</div></div>
  </div>
</section>

<section class="abs owner">
  <h2 class="section-title">ABOUT THE OWNER</h2>
  <div class="copy" style="margin-top:30px">
    <p>Lorem ipsum dolor sit amet, consectetur adipiscing elit. Duis a sapien venenatis, accumsan orci nec,</p>
    <p>convallis tellus. Suspendisse sed rutrum libero. Mauris gravida posuere lacus, eu faucibus magna rhoncus ut. Pellentesque quis nisl dapibus, euismod diam vel, elementum justo. Nunc imperdiet lectus sed mauris condimentum aliquet.</p>
  </div>
</section>

<section class="abs cta-band" role="img" aria-label="Blue-tinted photo of a person working at a laptop on a desk with plants"></section>
<h2 class="abs cta-title">Join Thousands of &nbsp;People<br>Around The World</h2>
<a class="abs cta-btn">Schedule an Inspection</a>

<footer class="abs site-footer">© 2019 by LodVenra. All rights reserved.</footer>
</body>
</html>
```